Design WORDPRESS Website for E Commerce Business

We are needing a WORDPRESS website for an E Commerce Business that is supplying quailty kids / baby products.

Target Market(s)

Female / Working Mums / New Mums

Industry/Entity Type

Business

Number of Pages Required

1 page

Font styles to use
Sans Serif

Colors
33b8a4
f8fcfd
d3a5cc
f7f1f7
cbcbcb
9d9d9d

```html
<!DOCTYPE html>
<html lang="en">
<head>
<meta charset="utf-8">
<title>Little Nest – Kids Products</title>
<link rel="stylesheet" href="https://fonts.googleapis.com/css2?family=Roboto:wght@300;400;500;700;900&display=swap">
<style>
:root{
  --teal:#33b8a4;
  --teal-dark:#2a9c8b;
  --pale:#f8fcfd;
  --pink:#d3a5cc;
  --pink-pale:#f7f1f7;
  --line:#cbcbcb;
  --mid:#9d9d9d;
  --ink:#3f3f3f;
  --dark:#2b2d31;
  --darker:#1f2124;
}
*{box-sizing:border-box;margin:0;padding:0}
html,body{width:1200px;height:3056px;overflow:hidden}
body{font-family:"Roboto",Arial,sans-serif;color:var(--ink);background:#fff;position:relative}
.abs{position:absolute}

/* hero */
.hero{left:0;top:0;width:1200px;height:1160px;overflow:hidden}
.hero-photo{left:0;top:0;width:1200px;height:1160px;background:linear-gradient(160deg,#5e554c 0%,#7b6e60 30%,#8e8377 55%,#6d665f 100%)}
.hero-fade{left:0;top:0;width:1200px;height:1160px}
.logo{left:96px;top:0;width:210px;height:100px;background:#fff;display:flex;align-items:center;justify-content:center;border-radius:0 0 6px 6px}
.logo-name{font-size:28px;font-weight:700;color:#555}
.nav{left:380px;top:24px;display:flex}
.nav a{display:block;padding:0 16px;height:44px;line-height:44px;color:#fff;font-size:15px;font-weight:500;text-decoration:none;text-transform:uppercase}
.nav a.active{background:var(--pink)}
.account{left:830px;top:36px;display:flex;gap:22px;color:#fff;font-size:13px}
.account span::before{content:"";display:inline-block;width:9px;height:9px;border-radius:50%;background:#fff;margin-right:6px;vertical-align:middle}
.order{left:1060px;top:22px;color:#fff;font-size:13px;line-height:17px;padding-left:30px}
.order::before{content:"";position:absolute;left:0;top:6px;width:22px;height:20px;border:2px solid #fff;border-radius:2px}
.tagline{left:360px;top:340px}
.tagline span{display:inline-block;background:var(--pink);color:#fff;font-weight:700;font-size:30px;text-transform:uppercase;padding:6px 14px;margin-bottom:6px;letter-spacing:.5px}
.search{left:380px;top:436px;width:480px;height:52px;display:flex}
.search input{flex:1;border:0;padding:0 18px;font-family:inherit;font-size:15px;color:var(--mid);background:#fff}
.search button{width:64px;border:0;background:var(--teal);display:flex;align-items:center;justify-content:center}
.welcome{left:88px;top:830px}
.welcome .pre{font-size:52px;font-weight:300;color:#555;letter-spacing:2px}
.welcome .brand{font-size:66px;font-weight:700;color:var(--pink);line-height:1;letter-spacing:1px}
.welcome .kind{font-size:66px;font-weight:700;color:#555;line-height:1.05}
.intro{left:724px;top:766px;width:400px;font-size:13px;line-height:19px;color:#555}
.intro p{margin-bottom:18px}
.btn{display:inline-block;background:var(--teal);color:#fff;font-size:12px;font-weight:500;text-transform:uppercase;padding:0 20px;height:36px;line-height:36px;text-decoration:none}
.more{left:724px;top:1050px}

/* products */
.section-title{width:1200px;left:0;text-align:center;font-size:48px;font-weight:300;color:#555;text-transform:uppercase}
.products-title{top:1214px}
.divider{left:460px;width:280px;height:2px;background:var(--line)}
.divider i{position:absolute;left:136px;top:-3px;width:8px;height:8px;border-radius:50%;background:var(--pink)}
.tabs{left:176px;top:1330px;display:flex}
.tabs a{width:170px;height:42px;line-height:40px;text-align:center;border:1px solid var(--line);margin-left:-1px;font-size:14px;color:#555;text-decoration:none;background:#fff}
.tabs a.active{background:var(--teal);border-color:var(--teal);color:#fff}
.grid{left:88px;top:1414px;width:1024px;display:grid;grid-template-columns:repeat(4,256px);grid-auto-rows:236px}
.photo{width:256px;height:236px}
.card{background:var(--pale);border:1px solid #eef2f3;padding:38px 30px}
.card h3{font-size:28px;font-weight:700;text-transform:uppercase;line-height:32px;color:#333}
.price{font-size:13px;color:var(--mid);margin:12px 0 14px}
.price b{font-size:24px;color:#444;font-weight:500;margin-left:8px}
.cart{display:inline-block;background:var(--pink);color:#fff;font-size:11px;padding:0 14px;height:28px;line-height:28px;border-radius:2px}
.cart::before{content:"";display:inline-block;width:8px;height:8px;border:1.5px solid #fff;margin-right:6px;vertical-align:-1px}
.view-all{left:496px;top:2400px;width:208px;text-align:center;padding:0}

/* contact */
.contact{left:0;top:2512px;width:1200px;height:544px;background:linear-gradient(180deg,#303237,#26282c)}
.contact-title{top:2572px;color:#fff}
.contact-divider{left:540px;top:2640px;width:120px;height:2px;background:#4d5056}
.contact-divider i{position:absolute;left:56px;top:-3px;width:8px;height:8px;border-radius:50%;background:var(--pink)}
.info{left:0;top:2676px;width:1200px;height:40px;background:rgba(0,0,0,.25);display:flex;justify-content:center;gap:70px;align-items:center;color:#ddd;font-size:15px}
.info span{display:flex;align-items:center;gap:10px}
.field{background:#fff;border:0;font-family:inherit;font-size:13px;color:var(--mid);padding:0 16px;width:420px;height:40px}
.f1{left:160px;top:2764px}.f2{left:160px;top:2820px}.f3{left:160px;top:2876px}
.message{left:612px;top:2764px;width:410px;height:116px;padding:14px 16px;resize:none}
.send{left:930px;top:2898px;width:92px;text-align:center}
.footer{left:0;top:3000px;width:1200px;height:56px;background:var(--darker);display:flex;align-items:center;justify-content:space-between;padding:0 88px;color:#777;font-size:11px}
.social{display:flex;gap:12px}
.social i{width:14px;height:14px;border-radius:50%;background:#5a5d63}
</style>
</head>
<body>

<section class="hero abs">
  <div class="hero-photo abs" role="img" aria-label="Photo of two young children standing together on a cobbled city street"></div>
  <svg class="hero-fade abs" width="1200" height="1160" viewBox="0 0 1200 1160">
    <defs>
      <linearGradient id="topShade" x1="0" y1="0" x2="0" y2="1">
        <stop offset="0" stop-color="#000" stop-opacity=".35"/>
        <stop offset="1" stop-color="#000" stop-opacity="0"/>
      </linearGradient>
    </defs>
    <rect width="1200" height="140" fill="url(#topShade)"/>
    <polygon points="0,760 1200,640 1200,1160 0,1160" fill="#eeeeee" opacity=".92"/>
  </svg>

  <div class="logo abs"><span class="logo-name">Little Nest</span></div>
  <nav class="nav abs">
    <a class="active" href="#">Home</a><a href="#">About</a><a href="#">Products</a><a href="#">Contact</a>
  </nav>
  <div class="account abs"><span>Create Account</span><span>Login</span></div>
  <div class="order abs">Your Order<br>$ 00.00</div>

  <h1 class="tagline abs"><span>Supplying quailty kids</span><br><span>baby products</span></h1>
  <form class="search abs">
    <input type="text" value="Search Products">
    <button type="button" aria-label="Search">
      <svg width="20" height="20" viewBox="0 0 20 20"><circle cx="8" cy="8" r="6" fill="none" stroke="#fff" stroke-width="2.4"/><line x1="12.5" y1="12.5" x2="18" y2="18" stroke="#fff" stroke-width="2.4"/></svg>
    </button>
  </form>

  <div class="welcome abs">
    <div class="pre">WELCOME TO</div>
    <div class="brand">LITTLE NEST</div>
    <div class="kind">KIDS PRODUCTS</div>
  </div>
  <div class="intro abs">
    <p>Lorem ipsum dolor sit amet consectetur adipiscing elit. Quisque gravida varius scelerisque. Sed posuere quam at felis sollicitudin et tincidunt ex consectetur. Sed quam urna, tempor a luctus in, euismod vel nunc. Duis vehicula massa eget dolor. Mauris id ultrices ex. Proin sit vehicula ipsum.</p>
    <p>Quisque gravida varius scelerisque. Sed posuere quam at felis sollicitudin et tincidunt ex consectetur. Sed quam urna, tempor a luctus in, euismod vel nunc. Duis vehicula massa eget dolor. Mauris id ultrices ex. Proin sit vehicula ipsum.</p>
  </div>
  <a class="btn more abs" href="#">More</a>
</section>

<h2 class="section-title products-title abs">Our Products</h2>
<div class="divider abs" style="top:1290px"><i></i></div>
<div class="tabs abs">
  <a class="active" href="#">All Items</a><a href="#">Baby</a><a href="#">Children cloth</a><a href="#">Teddy bear</a><a href="#">Toys</a>
</div>

<div class="grid abs">
  <div class="photo" role="img" aria-label="Mother pushing a baby carriage in a park" style="background:linear-gradient(135deg,#9bab7a,#6f5e4a)"></div>
  <div class="card"><h3>Baby<br>Carriage</h3><div class="price">PRICE: <b>$19.00</b></div><span class="cart">Add to cart</span></div>
  <div class="photo" role="img" aria-label="Toddler in a bunny costume next to a pram" style="background:linear-gradient(135deg,#cfc3b8,#a69383)"></div>
  <div class="card"><h3>Baby<br>Carriage</h3><div class="price">PRICE: <b>$19.00</b></div><span class="cart">Add to cart</span></div>

  <div class="card"><h3>Children<br>Clothes</h3><div class="price">PRICE: <b>$19.00</b></div><span class="cart">Add to cart</span></div>
  <div class="photo" role="img" aria-label="Child in a white knitted hat and red winter coat" style="background:linear-gradient(135deg,#b8222c,#7d1018)"></div>
  <div class="card"><h3>Children<br>Clothes</h3><div class="price">PRICE: <b>$19.00</b></div><span class="cart">Add to cart</span></div>
  <div class="photo" role="img" aria-label="Two children in colourful clothes against a blue background" style="background:linear-gradient(135deg,#5bb8e8,#2e86c8)"></div>

  <div class="photo" role="img" aria-label="Brown teddy bear on a turquoise background" style="background:linear-gradient(135deg,#63c3c0,#2d9a9a)"></div>
  <div class="card"><h3>Teddy Bear</h3><div class="price">PRICE: <b>$19.00</b></div><span class="cart">Add to cart</span></div>
  <div class="photo" role="img" aria-label="Toddler hugging a teddy bear in a car seat" style="background:linear-gradient(135deg,#4e5257,#9a9590)"></div>
  <div class="card"><h3>Teddy Bear</h3><div class="price">PRICE: <b>$19.00</b></div><span class="cart">Add to cart</span></div>

  <div class="card"><h3>Lorem Ipsum<br>Dolor</h3><div class="price">PRICE: <b>$19.00</b></div><span class="cart">Add to cart</span></div>
  <div class="photo" role="img" aria-label="Children playing with colourful toys in a playroom" style="background:linear-gradient(135deg,#e6e0d6,#c9a45a)"></div>
  <div class="card"><h3>Lorem Ipsum<br>Dolor</h3><div class="price">PRICE: <b>$19.00</b></div><span class="cart">Add to cart</span></div>
  <div class="photo" role="img" aria-label="Two toddlers playing happily with toy blocks" style="background:linear-gradient(135deg,#e9eef2,#8fb8d8)"></div>
</div>

<a class="btn view-all abs" href="#">View more all products</a>

<section class="contact abs"></section>
<h2 class="section-title contact-title abs">Contact Information</h2>
<div class="contact-divider abs"><i></i></div>
<div class="info abs">
  <span><svg width="16" height="16" viewBox="0 0 16 16"><path d="M3 1h3l1.5 4-2 1.2a9 9 0 0 0 4.3 4.3L11 8.5l4 1.5v3a2 2 0 0 1-2 2A12 12 0 0 1 1 3a2 2 0 0 1 2-2z" fill="var(--teal)"/></svg>123 - 456 - 789</span>
  <span><svg width="18" height="14" viewBox="0 0 18 14"><rect x="1" y="1" width="16" height="12" fill="none" stroke="var(--teal)" stroke-width="2"/><polyline points="1,1 9,8 17,1" fill="none" stroke="var(--teal)" stroke-width="2"/></svg>info@littlenest.com</span>
  <span><svg width="14" height="18" viewBox="0 0 14 18"><path d="M7 1a6 6 0 0 1 6 6c0 4-6 10-6 10S1 11 1 7a6 6 0 0 1 6-6z" fill="var(--teal)"/><circle cx="7" cy="7" r="2.2" fill="#2b2d31"/></svg>SM99 consectetur adipiscing elit, dolor sit amet</span>
</div>
<input class="field f1 abs" value="Name">
<input class="field f2 abs" value="Email Id">
<input class="field f3 abs" value="Phone Number">
<textarea class="field message abs">Message</textarea>
<a class="btn send abs" href="#">Send</a>

<footer class="footer abs">
  <span>© 2017 Little Nest. All rights reserved</span>
  <div class="social"><i></i><i></i><i></i><i></i><i></i></div>
</footer>

</body>
</html>
```